velumora.eu :: Design ideas (no coding) for key pages of Personalized greeting cards online store

We need your vision on modern, clean, easy to read user interface (UI) for online service of personalized printed products, like greeting cards, postcards, fridge magnets, clips and etc.
Your vision should include UI presentation for:
- Home page with login (including soc nets)
- Product Designer page
- Cart pages (products and address selection)
- Example of general internal page (pricing, terms, etc)
- Artist info and portfolio page
We are looking for ideas we will love, NOT complete design of a whole site.
Top design/vision will we used as a basement for separate contract on complete design of the site.

UI should be based on existing functionality with some extent. It should not break ideas or methods used on prototype but designers are free to offer own product presentations, designer’s layout and cart views.

Prototype:
English: http://velumora.eu
Russian: http://velumora.ru
Lithuanian: http://velumora.lt

Target Market(s)

People of 16-45 y.o. who likes to be distinctive, personal.

Industry/Entity Type

Store

Requirements
Must have
• Your work should meet attached requirements.
Site is multilingual. Wording should assume varieties in length on different languages.
Clean and easy to read UI
Flat design preferrably
Should be based on assets which are free or available for royalty-free licensing
Should not have
• heavy, meaningless 3D and shadow effects
Show NOT copy sites like: kindlow.com, tarnbell.co.uk

```html
<!DOCTYPE html>
<html lang="en">
<head>
<meta charset="utf-8">
<title>Velumora — Personalized greeting cards</title>
<link href="https://fonts.googleapis.com/css2?family=Lato:wght@300;400;700&display=swap" rel="stylesheet">
<style>
:root{
  --bg:#f8f6ee;
  --ink:#333;
  --muted:#777;
  --red:#d6402f;
  --dark-red:#b8261b;
  --orange-tab:#fbcd95;
  --line:#d9d7d0;
  --dark:#2b2b2b;
  --blue:#0a93cc;
  --yellow:#fcc72f;
  --grey-btn:#9b9b9b;
}
*{box-sizing:border-box;margin:0;padding:0}
html,body{width:862px;height:1200px;overflow:hidden}
body{background:var(--bg);font-family:"Lato",Arial,sans-serif;color:var(--ink);position:relative}
.abs{position:absolute}

.brand{left:86px;top:14px;display:flex;flex-direction:column;align-items:flex-start;gap:6px}
.brand-mark{width:56px;height:56px;background:var(--red)}
.brand-name{font-size:17px;font-weight:400;color:var(--dark-red)}

.sign-in{left:730px;top:30px;width:44px;height:19px;background:var(--dark);color:#fff;font-size:9px;display:flex;align-items:center;justify-content:center}
.top-links{left:511px;top:60px;font-size:12px;color:var(--muted);font-weight:300}
.top-links span{margin:0 8px;color:#aaa}
.cart-btn{left:629px;top:54px;width:83px;height:24px;background:var(--dark-red);color:#fff;font-size:9px;display:flex;align-items:center;justify-content:center;gap:6px}
.checkout-btn{left:712px;top:54px;width:62px;height:24px;background:var(--red);color:#fff;font-size:9px;display:flex;align-items:center;justify-content:center;gap:4px;border-left:1px solid #a21d14}
.caret{width:0;height:0;border-left:3px solid transparent;border-right:3px solid transparent;border-top:4px solid #fff}

.nav{left:86px;top:104px;width:688px;height:42px;display:flex;border:1px solid var(--line);background:#fbfaf5}
.nav a{display:flex;align-items:center;justify-content:center;font-size:12px;color:var(--ink);text-decoration:none;border-right:1px solid var(--line)}
.nav .active{background:var(--orange-tab)}
.nav .fav{background:var(--red);color:#fff;border:none;gap:6px}

.hero{left:86px;top:155px;width:688px;height:227px;background:linear-gradient(120deg,#e9e2d6 0%,#f1efe9 35%,#d9c9b4 60%,#e45a4a 80%,#eeeae2 100%)}
.hero-box{left:86px;top:211px;width:309px;height:106px;background:rgba(40,40,40,.78);color:#fff;padding:14px 20px}
.hero-box h1{font-weight:400;font-size:26px;line-height:1;margin-bottom:10px}
.hero-box p{font-size:9.5px;line-height:12px;font-weight:400}
.learn{left:86px;top:317px;width:115px;height:30px;background:var(--red);color:#fff;font-size:13px;display:flex;align-items:center;justify-content:center}

.filter-label{font-size:10px;color:var(--ink)}
.rule{height:1px;background:var(--line)}
.tags{left:86px;top:434px;width:450px;font-size:9.5px;line-height:20.5px}
.tags span{margin-right:10px}
.t-b{font-weight:700;font-size:11px}
.swatch{height:16px}
.reset{background:var(--grey-btn);color:#fff;font-size:9px;display:flex;align-items:center;justify-content:center}
.palette{left:587px;top:464px;width:186px;height:22px;background:#fff;border:1px solid #e2e0d9;display:flex;align-items:center;gap:6px;padding-left:6px}
.palette i{width:12px;height:12px;display:block}
.palette .sel{outline:2px solid #111;outline-offset:-2px}

.card{width:150px}
.card-img{width:150px;height:158px}
.card-bar{width:150px;height:3px;background:linear-gradient(90deg,#33469c 0 10%,#f07a1a 10% 20%,#0a93cc 20% 30%,#4c2f7e 30% 40%,#fcc72f 40% 50%,#8a9aa8 50% 60%,#d6402f 60% 70%,#f5b82f 70% 80%,#e06a2a 80% 90%,#5a8e2f 90% 100%)}
.card-meta{display:flex;justify-content:space-between;align-items:center;margin-top:10px;padding-left:0}
.price{color:var(--dark-red);font-weight:700;font-size:9.5px}
.chips{display:flex;gap:3px;margin-top:12px}
.chips span{background:#e6e4dd;font-size:7px;padding:2px 4px}
.grey-top{height:18px;background:#6f6f6f}

.load{left:0;width:862px;top:1020px;text-align:center;font-size:8px;color:var(--muted)}
.foot-rule{left:110px;top:1068px;width:652px;height:2px;background:#ecebe5}
.foot-links{left:0;width:862px;top:1089px;text-align:center;font-size:8.5px;color:#666}
.foot-links span{margin:0 5px;color:#bbb}
.socials{left:375px;top:1117px;display:flex;gap:4px}
.socials i{width:22px;height:22px;background:#e6e5e1;display:block}
.socials .on{background:#5bc7f2}
.copy{left:0;width:862px;top:1162px;text-align:center;font-size:7.5px;color:#777}
</style>
</head>
<body>

<div class="abs brand">
  <div class="brand-mark"></div>
  <div class="brand-name">velumora</div>
</div>

<div class="abs sign-in">Sign in</div>
<div class="abs top-links">Products<span>|</span>Authors</div>
<div class="abs cart-btn">
  <svg width="13" height="10" viewBox="0 0 13 10"><path d="M0 1h2l2 6h7l1.5-4.5H3.2" fill="none" stroke="#fff" stroke-width="1.2"/><circle cx="5" cy="9" r="1" fill="#fff"/><circle cx="10" cy="9" r="1" fill="#fff"/></svg>
  My Cart <span class="caret"></span>
</div>
<div class="abs checkout-btn">Checkout <span class="caret"></span></div>

<nav class="abs nav">
  <a style="width:57px">ALL</a>
  <a class="active" style="width:115px">Greeting cards</a>
  <a style="width:103px">Sound cards</a>
  <a style="width:91px">Postcards</a>
  <a style="width:85px">Magnets</a>
  <a style="width:120px">Wooden boards</a>
  <a class="fav" style="flex:1">
    <svg width="11" height="10" viewBox="0 0 11 10"><path d="M5.5 9.5 1 5C-.5 3.4.5.5 3 .5c1.2 0 2 .7 2.5 1.5C6 1.2 6.8.5 8 .5c2.5 0 3.5 2.9 2 4.5z" fill="#fff"/></svg>
    Favorites (0)
  </a>
</nav>

<div class="abs hero" role="img" aria-label="Photo of many fanned-out colourful greeting cards"></div>
<div class="abs hero-box">
  <h1>Welcome to Velumora</h1>
  <p>Lorem Ipsum is simply dummy text of the printing and typesetting industry. Lorem Ipsum has been the industry's standard dummy text .</p>
</div>
<div class="abs learn">Learn More</div>

<div class="abs filter-label" style="left:86px;top:408px">Theme</div>
<div class="abs filter-label" style="left:478px;top:408px">More ▾</div>
<div class="abs rule" style="left:86px;top:425px;width:434px"></div>
<div class="abs filter-label" style="left:586px;top:408px">Color</div>
<div class="abs rule" style="left:586px;top:425px;width:188px"></div>

<div class="abs tags">
  <span class="t-b" style="color:#8c5a2b">Backgrounds</span><span style="color:#e2522c">Bears</span><span style="color:#e84d8a">Best wishes</span><span style="color:#7ba22a">Birthday</span><span style="color:#1a73c9">Blue</span><span style="color:#2a66b8">Cards</span><span class="t-b" style="color:#8c5a2b">Cats</span><span style="color:#333">Christmas</span><span style="color:#8c7a3a">Christmas</span><br>
  <span style="color:#555">(catholic)</span><span class="t-b" style="color:#1e6b1e">Christmas (orthodox)</span><span style="color:#2a8a8a">Congratulations!</span><span class="t-b" style="color:#5a9e2a">Dogs</span><span style="color:#555">Easter</span><span style="color:#2a8ac9">Easter (orthodox)</span><br>
  <span class="t-b" style="color:#f07a1a">Flowers</span><span style="color:#c8a830">Food</span><span style="color:#2a66b8">For children</span><span class="t-b" style="color:#5a7e2a">Friendship</span><span style="color:#8c5a2b">Grey</span><span style="color:#b83a2a">Halloween</span><span class="t-b" style="color:#f07a1a">Love</span><span style="color:#3a5ab8">Miss you</span><span style="color:#444">New year</span>
</div>

<div class="abs swatch" style="left:586px;top:435px;width:57px;background:var(--blue)"></div>
<div class="abs swatch" style="left:647px;top:435px;width:58px;background:var(--yellow)"></div>
<div class="abs swatch reset" style="left:709px;top:435px;width:65px">Reset</div>
<div class="abs palette">
  <i style="background:#e84d8a"></i><i class="sel" style="background:#0a93cc"></i><i style="background:#5a9e1a"></i><i style="background:#a0703a"></i><i style="background:#f08a1a"></i><i style="background:#fcc72f"></i><i style="background:#3a9a9a"></i><i style="background:#c83a2a"></i><i style="background:#3a3a40"></i><i style="background:#5a4040"></i>
</div>

<!-- product grid -->
<div class="abs card" style="left:87px;top:520px">
  <div class="card-img" role="img" aria-label="Photo of a printed portrait postcard held by red fridge magnets" style="background:linear-gradient(135deg,#f2f0ec,#b9a48f 55%,#ece9e4)"></div>
  <div class="card-bar"></div>
  <div class="card-meta"><span class="price">$179.00</span><svg width="16" height="14" viewBox="0 0 16 14"><path d="M2 13V6L8 1l6 5v7" fill="none" stroke="#888" stroke-width="2"/></svg></div>
  <div class="chips"><span>Art House</span><span>Design</span><span>New year</span></div>
</div>
<div class="abs card" style="left:266px;top:520px">
  <div class="card-img" role="img" aria-label="Photo of a cream greeting card with a bell ornament print beside a tinsel tree" style="background:linear-gradient(160deg,#3e5b2a,#e8d8b8 45%,#6a5a4a)"></div>
  <div class="card-bar"></div>
  <div class="card-meta"><span class="price">$179.00</span><svg width="16" height="14" viewBox="0 0 16 14"><path d="M2 13V6L8 1l6 5v7" fill="none" stroke="#888" stroke-width="2"/></svg></div>
  <div class="chips"><span>Art House</span><span>Design</span><span>New year</span></div>
</div>
<div class="abs card" style="left:444px;top:520px">
  <div class="card-img" role="img" aria-label="Photo of a white winter greeting card with a small tree print" style="background:linear-gradient(160deg,#3e5b2a,#e6e8e4 45%,#5a5a5a)"></div>
  <div class="card-bar"></div>
  <div class="card-meta"><span class="price">$179.00</span><svg width="16" height="14" viewBox="0 0 16 14"><path d="M2 13V6L8 1l6 5v7" fill="none" stroke="#888" stroke-width="2"/></svg></div>
  <div class="chips"><span>Art House</span><span>Design</span><span>New year</span></div>
</div>
<div class="abs card" style="left:622px;top:520px">
  <div class="grey-top"></div>
  <div class="card-img" role="img" aria-label="Photo of a pink greeting card with a swirl pattern print" style="height:140px;background:linear-gradient(160deg,#3e5b2a,#d8c0b8 40%,#a8b098 70%,#e8a8a8)"></div>
  <div class="card-bar"></div>
  <div class="card-meta"><span class="price">$179.00</span><svg width="16" height="14" viewBox="0 0 16 14"><path d="M2 13V6L8 1l6 5v7" fill="none" stroke="#888" stroke-width="2"/></svg></div>
  <div class="chips"><span>Art House</span><span>Design</span><span>New year</span></div>
</div>

<div class="abs card" style="left:87px;top:762px">
  <div class="card-img" role="img" aria-label="Photo of a printed portrait postcard held by red fridge magnets" style="background:linear-gradient(135deg,#f2f0ec,#b9a48f 55%,#ece9e4)"></div>
  <div class="card-bar"></div>
  <div class="card-meta"><span class="price">$179.00</span><svg width="16" height="14" viewBox="0 0 16 14"><path d="M2 13V6L8 1l6 5v7" fill="none" stroke="#888" stroke-width="2"/></svg></div>
  <div class="chips"><span>Art House</span><span>Design</span><span>New year</span></div>
</div>
<div class="abs card" style="left:266px;top:762px">
  <div class="card-img" role="img" aria-label="Photo of a cream greeting card with a bell ornament print beside a tinsel tree" style="background:linear-gradient(160deg,#3e5b2a,#e8d8b8 45%,#6a5a4a)"></div>
  <div class="card-bar"></div>
  <div class="card-meta"><span class="price">$179.00</span><svg width="16" height="14" viewBox="0 0 16 14"><path d="M2 13V6L8 1l6 5v7" fill="none" stroke="#888" stroke-width="2"/></svg></div>
  <div class="chips"><span>Art House</span><span>Design</span><span>New year</span></div>
</div>
<div class="abs card" style="left:444px;top:762px">
  <div class="card-img" role="img" aria-label="Photo of a white winter greeting card with a small tree print" style="background:linear-gradient(160deg,#3e5b2a,#e6e8e4 45%,#5a5a5a)"></div>
  <div class="card-bar"></div>
  <div class="card-meta"><span class="price">$179.00</span><svg width="16" height="14" viewBox="0 0 16 14"><path d="M2 13V6L8 1l6 5v7" fill="none" stroke="#888" stroke-width="2"/></svg></div>
  <div class="chips"><span>Art House</span><span>Design</span><span>New year</span></div>
</div>
<div class="abs card" style="left:622px;top:762px">
  <div class="grey-top"></div>
  <div class="card-img" role="img" aria-label="Photo of a pink greeting card with a swirl pattern print" style="height:140px;background:linear-gradient(160deg,#3e5b2a,#d8c0b8 40%,#a8b098 70%,#e8a8a8)"></div>
  <div class="card-bar"></div>
  <div class="card-meta"><span class="price">$179.00</span><svg width="16" height="14" viewBox="0 0 16 14"><path d="M2 13V6L8 1l6 5v7" fill="none" stroke="#888" stroke-width="2"/></svg></div>
  <div class="chips"><span>Art House</span><span>Design</span><span>New year</span></div>
</div>

<div class="abs load">⁞⁞ Loard More...</div>

<footer>
  <div class="abs foot-rule"></div>
  <div class="abs foot-links">Home<span>•</span>All medias<span>•</span>Greeting cards<span>•</span>Square cards<span>•</span>Postcards<span>•</span>NEW Products<span>•</span>Checkout<span>•</span>Contact Us</div>
  <div class="abs socials" aria-label="Social links">
    <i class="on"></i><i></i><i></i><i></i><i></i>
  </div>
  <div class="abs copy">© 2013 COPYRIGHT VELUMORA - ALL RIGHTS RESERVED</div>
</footer>

</body>
</html>
```